Wordpress website design for a high-end painting business

We are currently rebranding and are looking to update our Wordpress theme. We have recently rebranded our logo on ArtHatchery, and would like our website to be equally as refined.
Our business is named “Holloway Coatings”. We are a high-end painting business that is known for being professional and having high standards. Our clean and professional image is important as it separates us from our competition. Our current website can be found at www.hollowayfinishes.co.nz . We designed the site ourselves so it is understandably rudimentary. We are generally happy with the. page layout of our existing site, but we like a professional remodel. Any ideas on improvement welcomed.
We would like the front page of the website to summarise all of the info throughout the whole website (I.e introduction, photos, testimonials, contact info etc.) as visitors typically scroll through the first page to see that we are reputable and get to our contact number/email contact at the bottom of the page. We would like this first page to give a clean well rounded image of our business. We would like the gallery to be a scroll through of large photos, as it is difficult to see paint details in smaller photos. A contact page with an enquiry section would also be good.
For the colour scheme, we would like something that fits a bold, masculine and high end theme (similar to our logo attached).
We would like the footer to include Velnor paint logos and the accredited painter logo we have included as these are important to our profession.
We have attached some photos of our work also. I will add more in the coming days. More can also be found on our website.
If you have questions or comments, please don’t hesitate to ask and I will get back as soon as possible.
We are open to your own interpretation or ideas for a better layout/site provided they fit the general brief of being a well rounded site for our profession.
Thanks,
Holloway Coatings.
Target Market(s)
High end clients
Industry/Entity Type
Painting (interior and exterior)
Coding
Coded - Design and coding required
Requirements
Must have
- Classy feel, separating us from typical painting companies. Well rounded homepage.
Nice to have
- Lots of examples of our work
Should not have
- Untidy paint motifs (eg, paint droplets, paint splashes)

```html
<!DOCTYPE html>
<html lang="en">
<head>
<meta charset="utf-8">
<title>Holloway Coatings — High Quality Paint-Work</title>
<link href="https://fonts.googleapis.com/css2?family=Roboto+Slab:wght@400;500;700&family=Roboto:wght@400;500;700&family=Montserrat:wght@600;700&display=swap" rel="stylesheet">
<style>
:root{
  --tan:#a8875a;
  --tan-light:#c9a574;
  --cream:#f6d9b3;
  --navy:#1c2535;
  --navy-deep:#0f1f38;
  --blue:#1d4a78;
  --blue-dark:#0f2d4d;
  --ink:#222;
  --muted:#555;
  --grey:#e9e7e8;
  --pill:#d8d8d8;
  --white:#fff;
  --slab:"Roboto Slab",serif;
  --sans:"Roboto",sans-serif;
  --caps:"Montserrat",sans-serif;
}
*{box-sizing:border-box;margin:0;padding:0}
html,body{width:1200px;height:4468px;overflow:hidden}
body{position:relative;font-family:var(--sans);color:var(--ink);background:var(--white)}
.abs{position:absolute}
.btn{position:absolute;display:flex;align-items:center;justify-content:center;border:2px solid var(--ink);border-radius:30px;background:var(--white);font-family:var(--slab);font-size:16px;color:var(--ink);box-shadow:0 4px 6px rgba(0,0,0,.25)}
.photo{position:absolute;box-shadow:0 6px 14px rgba(0,0,0,.25);border:4px solid var(--white)}

/* top bar */
.topbar{left:0;top:0;width:1200px;height:31px;background:var(--tan);color:var(--white);font-size:14px}
.topbar .mail{position:absolute;left:160px;top:7px;display:flex;gap:8px;align-items:center}
.topbar .follow{position:absolute;right:160px;top:7px;display:flex;gap:12px;align-items:center}
.dot{width:10px;height:10px;border-radius:50%;background:var(--white);display:inline-block}

/* header */
.header{left:0;top:31px;width:1200px;height:68px;background:var(--white)}
.nav{position:absolute;left:328px;top:24px;display:flex;gap:22px;font-size:14px;color:var(--muted)}
.nav .active{color:var(--ink);font-weight:500}
.estimate{position:absolute;left:815px;top:0;width:385px;height:68px;background:var(--navy);clip-path:polygon(8% 0,100% 0,100% 100%,0 100%)}
.estimate .label{position:absolute;left:84px;top:14px;font-size:10px;color:var(--white);font-family:var(--slab)}
.estimate .num{position:absolute;left:84px;top:30px;font-size:18px;color:var(--tan-light);letter-spacing:1px}
.logo-tab{left:153px;top:31px;width:140px;height:140px;background:var(--white);clip-path:polygon(0 0,100% 0,90% 100%,10% 100%);display:flex;flex-direction:column;align-items:center;justify-content:flex-end;padding-bottom:20px;z-index:3}
.logo-tab .mark{display:block;width:58px;height:58px;border:2px solid var(--navy);border-radius:50%;margin-bottom:10px}
.logo-tab .name{font-family:var(--slab);font-weight:700;font-size:15px;color:var(--navy);text-align:center;line-height:1.15}

/* hero */
.hero{left:0;top:99px;width:1200px;height:539px;background:linear-gradient(135deg,#8d8a84 0%,#c9c6c0 40%,#a9a39a 75%,#6f6a62 100%)}
.hero-disc{left:583px;top:148px;width:450px;height:450px;border-radius:50%;background:rgba(40,48,60,.88);box-shadow:0 0 0 10px rgba(40,48,60,.35)}
.hero-title{left:583px;top:250px;width:450px;text-align:center;font-family:var(--slab);font-weight:400;font-size:52px;line-height:64px;color:var(--white);white-space:nowrap}
.hero-arrow{top:383px;width:18px;height:18px;border-top:3px solid var(--white);border-right:3px solid var(--white)}

/* about */
.about-ring{left:160px;top:749px;width:375px;height:375px;border-radius:50%;border:4px solid var(--cream)}
.about-photo{left:205px;top:790px;width:290px;height:290px;border-radius:50%;background:linear-gradient(160deg,#b9c3cc,#7c8a74 60%,#9b4b3c);border:8px solid #f1f1f1;box-shadow:0 6px 18px rgba(0,0,0,.2)}
.about-sym{left:428px;top:835px;width:220px;height:190px;border-radius:50%;background:linear-gradient(135deg,#e4d3bc,#c9a574)}
.about h2{position:absolute;left:683px;top:752px;font-family:var(--slab);font-weight:400;font-size:48px;color:var(--ink)}
.about p{position:absolute;left:683px;width:360px;font-size:13.5px;line-height:22px;color:var(--ink)}

/* services */
.services{left:0;top:1231px;width:1200px;height:635px;background:radial-gradient(ellipse at 50% 50%,var(--blue) 0%,var(--blue-dark) 100%)}
.sec-title{position:absolute;width:1200px;text-align:center;font-family:var(--slab);font-weight:400;font-size:50px}
.services .sec-title{top:48px;color:var(--white)}
.centre-logo{left:472px;top:229px;width:260px;height:260px;border-radius:50%;background:var(--white);box-shadow:0 0 0 8px rgba(255,255,255,.2);display:flex;flex-direction:column;align-items:center;justify-content:center;font-family:var(--slab);font-weight:700;color:var(--navy);font-size:30px;line-height:1.1}
.centre-logo span{font-size:17px;letter-spacing:4px;font-weight:700}
.pill{position:absolute;width:270px;height:111px;border-radius:56px;background:var(--pill);font-family:var(--slab);font-size:20px;line-height:26px;color:var(--ink);display:flex;align-items:center;box-shadow:0 4px 10px rgba(0,0,0,.3)}
.pill.left{left:160px;padding-left:138px}
.pill.right{left:756px;justify-content:flex-end;padding-right:138px;text-align:right}
.pill.hot{background:linear-gradient(90deg,#b07a3c,#c9914e);color:var(--white);padding:0 24px;text-align:center;justify-content:center}
.pill .thumb{position:absolute;top:0;width:111px;height:111px;border-radius:50%;background:var(--white);display:flex;align-items:center;justify-content:center}
.pill.left .thumb{left:0}.pill.right .thumb{right:0}
.pill .thumb i{display:block;width:95px;height:95px;border-radius:50%;border:2px solid #444}

/* gallery */
.gallery h2{position:absolute;left:158px;top:1932px;font-family:var(--slab);font-weight:400;font-size:50px}
.caption{position:absolute;left:0;bottom:0;width:100%;height:76px;background:rgba(168,135,90,.88);color:var(--white);font-family:var(--slab);font-size:18px;display:flex;align-items:center;padding-left:20px}

/* testimonials */
.testi{left:0;top:2903px;width:1200px;height:610px;background:var(--navy)}
.testi .sec-title{top:68px;color:var(--white)}
.card{position:absolute;top:163px;width:276px;height:281px;background:#3b3f48;border-radius:0 0 70px 0;padding:46px 28px 0;color:#e5e5e5}
.card.hot{background:linear-gradient(160deg,#b78346,#d7a566)}
.card .q{font-family:var(--slab);font-size:32px;line-height:20px;color:var(--tan-light);font-weight:700}
.card.hot .q{color:var(--white)}
.card p{margin-top:12px;font-size:15.5px;line-height:22px}
.card .who{margin-top:28px;font-family:var(--caps);font-weight:700;font-size:16px;line-height:26px;letter-spacing:.5px;color:var(--white)}
.card.hot .who{color:#fbe6c8}
.card .go{position:absolute;left:208px;top:213px;width:36px;height:36px;border-radius:50%;background:var(--white);display:flex;align-items:center;justify-content:center}

/* quote */
.quote{left:0;top:3513px;width:1200px;height:498px;background:var(--grey);overflow:hidden}
.quote h2{position:absolute;left:157px;top:50px;font-family:var(--slab);font-weight:400;font-size:50px;color:var(--ink)}
.field{position:absolute;background:var(--white);border:1px solid #9a9a9a;font-size:13px;color:#333;padding:12px 10px}
.quote-art{left:790px;top:20px;width:520px;height:520px;border-radius:50%;background:radial-gradient(circle at 50% 40%,#ffffff 0%,#f4f2f2 70%)}
.quote-fig{left:900px;top:170px;width:300px;height:220px;border-radius:40% 0 0 50%;background:linear-gradient(120deg,#b08a5e,#6f7277)}

/* footer */
.footer{left:0;top:4011px;width:1200px;height:457px;background:var(--navy-deep);color:var(--white)}
.footer h4{position:absolute;top:118px;font-family:var(--slab);font-weight:400;font-size:16px;color:var(--tan)}
.footer .list{position:absolute;top:158px;font-size:14.5px;line-height:31.5px}
.footer .info{position:absolute;display:flex;gap:14px;align-items:center;font-size:14px;line-height:20px}
.ico{width:28px;height:28px;border-radius:50%;background:var(--tan);flex:none;display:flex;align-items:center;justify-content:center}
.footer .social{position:absolute;left:160px;top:296px;display:flex;gap:10px}
.footer .social i{width:26px;height:26px;border-radius:50%;background:var(--tan);display:block}
.f-logo{position:absolute;left:160px;top:116px;width:118px;text-align:center}
.f-logo .mark{display:block;width:96px;height:96px;border-radius:50%;border:3px solid var(--white);margin:0 auto 12px}
.f-logo .name{font-family:var(--slab);font-weight:700;font-size:17px;line-height:20px}
.copy{position:absolute;left:160px;top:392px;font-size:12px;color:#c8c8c8}
.copy b{font-weight:400;color:var(--tan)}
</style>
</head>
<body>

<div class="abs topbar">
  <div class="mail"><svg width="14" height="10" viewBox="0 0 14 10"><rect x="0.5" y="0.5" width="13" height="9" fill="none" stroke="#fff"/><path d="M0.5 0.5 7 6 13.5 0.5" fill="none" stroke="#fff"/></svg>studio@hollowaycoatings.co.nz</div>
  <div class="follow">Follow Us : <i class="dot"></i><i class="dot"></i><i class="dot"></i></div>
</div>

<div class="abs header">
  <nav class="nav"><span class="active">Home</span><span>About</span><span>Services</span><span>Gallery</span><span>All Testimonials</span><span>Contact</span></nav>
  <div class="estimate">
    <svg class="abs" style="left:46px;top:22px" width="22" height="22" viewBox="0 0 24 24"><path d="M6 3l3 5-2 2c1 2 3 4 5 5l2-2 5 3-2 4C10 20 4 14 2 7z" fill="none" stroke="#fff" stroke-width="1.4"/></svg>
    <div class="label">Schedule A Painting Estimate</div>
    <div class="num">021 - 555 - 0193</div>
  </div>
</div>
<div class="abs logo-tab"><i class="mark"></i><div class="name">HOLLOWAY<br>COATINGS</div></div>

<section class="abs hero" role="img" aria-label="Photo of a freshly painted empty room with polished concrete floor and sliding doors"></section>
<div class="abs hero-disc"></div>
<h1 class="abs hero-title">The Highest<br>Quality<br>Paint-Work</h1>
<div class="btn" style="left:730px;top:460px;width:144px;height:54px;border-color:#fff;background:rgba(40,48,60,.9);color:#fff;font-family:var(--slab);font-size:15px">Contact Us</div>
<i class="abs hero-arrow" style="left:124px;transform:rotate(-135deg)"></i>
<i class="abs hero-arrow" style="left:1072px;transform:rotate(45deg)"></i>

<section class="about">
  <div class="abs about-ring"></div>
  <div class="abs about-photo" role="img" aria-label="Photo of a worker waterblasting a red roof"></div>
  <div class="abs about-sym" role="img" aria-label="Brand emblem decoration"></div>
  <i class="abs" style="left:464px;top:792px;width:12px;height:12px;border-radius:50%;background:var(--tan)"></i>
  <i class="abs" style="left:490px;top:1042px;width:12px;height:12px;border-radius:50%;background:var(--tan)"></i>
  <h2>About Us</h2>
  <p style="top:825px">Here at Holloway Coatings, we take a lot of pride in our work. We strive to ensure the highest quality paint-work, paying close attention to detail to provide a long lasting finish.</p>
  <p style="top:932px">Here at Holloway Coatings, we take a lot of pride in our work. We strive to ensure the highest quality paint-work, paying close attention to detail to provide a long lasting finish.</p>
  <div class="btn" style="left:683px;top:1049px;width:144px;height:50px">Read More</div>
</section>

<section class="abs services">
  <h2 class="sec-title">Our Services</h2>
  <div class="abs centre-logo">HOLLOWAY<span>COATINGS</span></div>
  <div class="pill left" style="top:157px"><div class="thumb" role="img" aria-label="Photo of a house exterior"><i style="background:linear-gradient(#c6d3de,#6c8a5a)"></i></div>Exterior<br>Painting</div>
  <div class="pill left" style="top:294px"><div class="thumb" role="img" aria-label="Photo of an interior room"><i style="background:linear-gradient(#e6e1da,#8a6b55)"></i></div>Interior<br>Painting</div>
  <div class="pill left" style="top:430px"><div class="thumb" role="img" aria-label="Photo of patterned wallpaper"><i style="background:linear-gradient(#9aa39b,#6c7670)"></i></div>Wall<br>papering</div>
  <div class="pill right" style="top:157px"><div class="thumb" role="img" aria-label="Photo of plastering work"><i style="background:linear-gradient(#8f8f8f,#d9c8b6)"></i></div>Plastering</div>
  <div class="pill right hot" style="top:294px">Waterblasting &amp; House Cleaning</div>
  <div class="pill right" style="top:430px"><div class="thumb" role="img" aria-label="Photo of a painted roof"><i style="background:linear-gradient(#c7ccd3,#6f747a)"></i></div>Roof<br>Painting</div>
</section>

<section class="gallery">
  <h2>Gallery</h2>
  <div class="photo" style="left:160px;top:2037px;width:440px;height:236px;background:linear-gradient(120deg,#e8e8e6,#cfcac2)" role="img" aria-label="Photo of a freshly painted empty room"></div>
  <div class="photo" style="left:720px;top:1994px;width:320px;height:238px;background:linear-gradient(150deg,#eceae6,#b9b4ab)" role="img" aria-label="Photo of a painted lounge with fireplace"></div>
  <div class="photo" style="left:160px;top:2318px;width:270px;height:401px;background:linear-gradient(180deg,#f2f2f2 0%,#e2e2e2 65%,#8a4a33 100%)" role="img" aria-label="Photo of white weatherboard exterior wall"></div>
  <div class="photo" style="left:713px;top:2448px;width:322px;height:240px;background:linear-gradient(160deg,#efece8,#a9a39b)" role="img" aria-label="Photo of a painted kitchen"></div>
  <div class="photo" style="left:381px;top:2112px;width:571px;height:428px;border-width:6px;background:linear-gradient(180deg,#c9d0d6 0%,#8d9ba8 45%,#6d8a52 80%,#58703f 100%);box-shadow:0 10px 24px rgba(0,0,0,.35)" role="img" aria-label="Photo of a repainted grey weatherboard house">
    <div class="caption">Exterior repaint in Te Kauwhata, Waikato.</div>
  </div>
  <div class="btn" style="left:529px;top:2767px;width:142px;height:50px">View All</div>
</section>

<section class="abs testi">
  <h2 class="sec-title">Testimonial</h2>
  <div class="card" style="left:160px"><div class="q">&ldquo;</div><p>Mason and his Team have done an amazing job painting our house. &rdquo;</p><div class="who">MARTA KOWALEWSKA<br>(2019)</div><div class="go"><svg width="16" height="14" viewBox="0 0 16 14"><path d="M1 7h12M8 2l5 5-5 5" fill="none" stroke="#1c2535" stroke-width="2.2"/></svg></div></div>
  <div class="card hot" style="left:461px"><div class="q">&ldquo;</div><p>Very happy with Holloway decorators. Mason and Rowan did a great job. &rdquo;</p><div class="who">PETER LINDQVIST<br>(2020)</div><div class="go"><svg width="16" height="14" viewBox="0 0 16 14"><path d="M1 7h12M8 2l5 5-5 5" fill="none" stroke="#b78346" stroke-width="2.2"/></svg></div></div>
  <div class="card" style="left:765px"><div class="q">&ldquo;</div><p>Mason and Rowan was prompt and efficient. Very friendly . &rdquo;</p><div class="who">DANIEL MOREAU<br>(2020)</div><div class="go"><svg width="16" height="14" viewBox="0 0 16 14"><path d="M1 7h12M8 2l5 5-5 5" fill="none" stroke="#1c2535" stroke-width="2.2"/></svg></div></div>
  <div class="btn" style="left:529px;top:497px;width:142px;height:50px;border-color:#fff;background:var(--navy);color:#fff">View All</div>
</section>

<section class="abs quote">
  <div class="abs quote-art"></div>
  <div class="abs quote-fig" role="img" aria-label="Brand emblem illustration"></div>
  <h2>Request A Online Quote</h2>
  <div class="field" style="left:158px;top:123px;width:289px;height:42px">Name :</div>
  <div class="field" style="left:453px;top:123px;width:289px;height:42px">Phone</div>
  <div class="field" style="left:158px;top:174px;width:289px;height:41px">Email :</div>
  <div class="field" style="left:453px;top:174px;width:289px;height:41px">Address :</div>
  <div class="field" style="left:158px;top:226px;width:584px;height:41px">Service :<svg class="abs" style="right:12px;top:16px" width="10" height="8" viewBox="0 0 10 8"><path d="M0 0h10L5 8z" fill="#222"/></svg></div>
  <div class="field" style="left:158px;top:276px;width:584px;height:107px">Message :</div>
  <div class="btn" style="left:160px;top:397px;width:143px;height:52px">Send Message</div>
</section>

<footer class="abs footer">
  <div class="f-logo"><i class="mark"></i><div class="name">HOLLOWAY<br>COATINGS</div></div>
  <div class="social"><i></i><i></i><i></i></div>
  <h4 style="left:349px">Quick Link</h4>
  <div class="list" style="left:349px">Home<br>About<br>Services<br>Gallery<br>All Testimonials<br>Contact</div>
  <h4 style="left:522px">Location</h4>
  <div class="info" style="left:522px;top:160px"><span class="ico"><svg width="12" height="16" viewBox="0 0 12 16"><path d="M6 15C2 9 1 7.5 1 5.5a5 5 0 0 1 10 0C11 7.5 10 9 6 15z" fill="#fff"/><circle cx="6" cy="5.5" r="2" fill="#a8875a"/></svg></span><span>Rowan Ashby<br>Hamilton, Waikato.</span></div>
  <div class="info" style="left:522px;top:231px"><span class="ico"><svg width="14" height="14" viewBox="0 0 24 24"><path d="M6 3l3 5-2 2c1 2 3 4 5 5l2-2 5 3-2 4C10 20 4 14 2 7z" fill="#fff"/></svg></span><span>021 555 0193</span></div>
  <div class="info" style="left:522px;top:280px"><span class="ico"><svg width="14" height="10" viewBox="0 0 14 10"><rect x="0.5" y="0.5" width="13" height="9" fill="#fff"/><path d="M0.5 0.5 7 6 13.5 0.5" fill="none" stroke="#a8875a"/></svg></span><span>studio@hollowaycoatings.co.nz</span></div>
  <h4 style="left:787px">Newsletter Sign Up</h4>
  <div class="abs" style="left:789px;top:158px;width:250px;font-size:14px;line-height:22px">Get weekly access to our best deals</div>
  <div class="abs" style="left:789px;top:203px;width:252px;height:44px;background:#fff;border-radius:4px;color:#333;font-size:14px;padding:13px 34px">Enter Mail Id</div>
  <div class="abs" style="left:789px;top:258px;width:143px;height:50px;border:2px solid #fff;border-radius:26px;display:flex;align-items:center;justify-content:center;font-size:15px">Subscribe Now</div>
  <div class="copy">Copyright © 2022 <b>Holloway Coatings.</b> All Right Reserved</div>
  <div class="abs" style="left:659px;top:373px;width:112px;height:38px;background:#2a3f7a;border-radius:3px" role="img" aria-label="Velnor paint badge"></div>
  <div class="abs" style="left:775px;top:373px;width:215px;height:38px;background:#2c9ad6;border-radius:3px" role="img" aria-label="Accredited painter badge"></div>
  <div class="abs" style="left:1000px;top:373px;width:38px;height:38px;border:3px solid #2c9ad6;border-radius:3px"></div>
</footer>

</body>
</html>
```